I need this done FAST!
Business Cards and Stationary for new home construction company - Construction
Simple
Gerald Finch
Owner
4816 Marlow Ct #306142 Houston, TX 77391
Gerald@thequillstoneframeworks.com
www.thequillstoneframeworks.com
I would like this business card to be minimal in its design. I just want it to be a way of saying ... Hi, call me directly. It does not need to be an advertisement. I need the vector files of this please
Front should be the logo only, and the back should be this information: Design~Build Firm Gerald Finch, Owner Phone Email Web address

```html
<!DOCTYPE html>
<html lang="en">
<head>
<meta charset="utf-8">
<title>Quillstone Frameworks — Business Cards</title>
<link rel="stylesheet" href="https://fonts.googleapis.com/css2?family=Roboto:ital,wght@0,400;0,700;1,400&display=swap">
<style>
  :root {
    --backdrop: #e4e4e6;
    --card: #ffffff;
    --red: #d0141c;
    --red-dark: #9e0b12;
    --ink: #3a3a3c;
    --muted: #6b6b6e;
    --silver: #cfd0d3;
  }
  * { margin: 0; padding: 0; box-sizing: border-box; }
  html, body { width: 1200px; height: 871px; overflow: hidden; }
  body {
    background: var(--backdrop);
    font-family: "Roboto", Arial, sans-serif;
    color: var(--ink);
    position: relative;
  }
  .card {
    position: absolute;
    width: 560px;
    height: 320px;
    background: var(--card);
    box-shadow: 0 6px 18px rgba(0,0,0,.18);
    overflow: hidden;
  }
  .card-front { left: 320px; top: 70px; }
  .card-back  { left: 320px; top: 450px; }

  .brand { display: flex; flex-direction: column; align-items: center; }
  .brand-name {
    display: flex; align-items: center; gap: 10px;
    font-weight: 700; color: var(--ink); letter-spacing: 1px;
  }
  .brand-mark { width: 18px; height: 18px; background: var(--red); flex: none; }
  .brand-words span + span { margin-left: .3em; }
  .brand-tagline { color: var(--muted); font-size: 9px; letter-spacing: 2px; margin-top: 6px; }

  .card-front .brand { position: absolute; inset: 0; justify-content: center; }
  .card-front .brand-name { font-size: 30px; }

  .card-back .brand { position: absolute; right: 40px; top: 96px; width: 190px; }
  .card-back .brand-name { font-size: 21px; line-height: 1.1; gap: 10px; }
  .card-back .brand-mark { width: 22px; height: 22px; }
  .card-back .brand-words span { display: block; }
  .card-back .brand-words span + span { margin-left: 0; }
  .card-back .brand-tagline { font-size: 7px; margin-top: 8px; }

  .contact { position: absolute; left: 34px; top: 30px; width: 250px; }
  .contact-name { color: var(--red); font-style: italic; font-size: 17px; }
  .contact-title { color: var(--muted); font-size: 10px; margin-top: 2px; }
  .contact-list { list-style: none; margin-top: 16px; }
  .contact-list li {
    display: flex; align-items: center; gap: 8px;
    font-size: 10.5px; color: var(--ink); margin-bottom: 7px;
    white-space: nowrap;
  }
  .icon {
    width: 14px; height: 14px; border-radius: 50%;
    background: var(--red); flex: none;
    display: flex; align-items: center; justify-content: center;
  }
  .icon svg { width: 8px; height: 8px; fill: #fff; }
  .contact-address { font-size: 10.5px; color: var(--ink); margin-top: 8px; white-space: nowrap; }

  .swoosh { position: absolute; left: 0; bottom: 0; width: 560px; height: 110px; }
</style>
</head>
<body>

<section class="card card-front" aria-label="Card front">
  <div class="brand">
    <div class="brand-name"><span class="brand-mark"></span><span class="brand-words"><span>QUILLSTONE</span><span>FRAMEWORKS</span></span></div>
    <div class="brand-tagline">PLAN IT • FRAME IT • BUILD IT</div>
  </div>
</section>

<section class="card card-back" aria-label="Card back">
  <div class="contact">
    <p class="contact-name">Gerald Finch</p>
    <p class="contact-title">Owner</p>
    <ul class="contact-list">
      <li><span class="icon"><svg viewBox="0 0 10 10"><path d="M2 1h2l1 2-1 1a5 5 0 0 0 2 2l1-1 2 1v2c-4 1-8-3-7-7z"/></svg></span>713 555 0148</li>
      <li><span class="icon"><svg viewBox="0 0 10 10"><path d="M1 2h8v6H1z"/></svg></span>Gerald@thequillstoneframeworks.com</li>
      <li><span class="icon"><svg viewBox="0 0 10 10"><circle cx="5" cy="5" r="4"/></svg></span>www.thequillstoneframeworks.com</li>
    </ul>
    <p class="contact-address">4816 Marlow Ct #306142 Houston, TX 77391</p>
  </div>

  <div class="brand">
    <div class="brand-name"><span class="brand-mark"></span><span class="brand-words"><span>QUILLSTONE</span><span>FRAMEWORKS</span></span></div>
    <div class="brand-tagline">PLAN IT • FRAME IT • BUILD IT</div>
  </div>

  <svg class="swoosh" viewBox="0 0 560 110" preserveAspectRatio="none" aria-hidden="true">
    <path d="M0 40 C180 95 360 95 560 20 L560 110 L0 110 Z" fill="var(--silver)"/>
    <path d="M0 55 C180 105 380 100 560 38 L560 110 L0 110 Z" fill="var(--red-dark)"/>
    <path d="M0 62 C190 110 390 108 560 48 L560 110 L0 110 Z" fill="var(--red)"/>
  </svg>
</section>

</body>
</html>
```